re brand of safeguardly.pro to Vexawatch.co.uk

We would like a new site design for our safeguardly.pro site

the new domain is Vexawatch.co.uk

we like the blue colour smiler to this site http://www.fundsentrypal.co.uk, and we would like real images o people using instead of cartons

you can take inspiration from the credit ref agency monthly membership site but this product is not a credit report we just like that look

https://www.loanharbor.co.uk
http://www.fundsentrypal.co.uk/
https://www.brimzo.co.uk/

Reason: we have added more details to the project brief and also increased the budget and committed to buying a design

We have guaranteed the project extend the dead line and increased the payment we have also added more details in the brief to give you guys more direction I am looking forward to seeing the designs

Target Market(s)

18 to 50 yo concerned with the privacy and id fraud

The bulk of clients our aged 18 to 30 so a fresh feel is important

Industry/Entity Type

Domain

Colors
33a6d7
0592cd
0555a3
3176b5
85cae6

```html
<!DOCTYPE html>
<html lang="en">
<head>
<meta charset="utf-8">
<title>Vexawatch.co.uk – Social Alert</title>
<link href="https://fonts.googleapis.com/css2?family=Open+Sans:wght@300;400;600;700&display=swap" rel="stylesheet">
<style>
:root{
  --blue:#049dd9;
  --blue-dark:#0592cd;
  --green:#5cc43d;
  --green-dark:#4aa92e;
  --navy:#1c2433;
  --ink:#333a40;
  --text:#666b70;
  --muted:#888;
  --band:#eef1f2;
  --white:#fff;
}
*{margin:0;padding:0;box-sizing:border-box}
html,body{width:1200px;height:1159px;overflow:hidden;background:var(--white);font-family:"Open Sans",Arial,sans-serif}
.page{position:relative;width:1200px;height:1159px}
.site-header{position:absolute;top:0;left:0;width:1200px;height:69px}
.brand{position:absolute;left:151px;top:20px;display:flex;align-items:center;gap:9px;font-size:20px;font-weight:400;color:#555c63;letter-spacing:.2px}
.brand-dot{width:30px;height:30px;border-radius:50%;background:var(--blue)}
.main-nav{position:absolute;left:537px;top:25px;display:flex;gap:17px;font-size:12.5px;color:#777;white-space:nowrap}
.main-nav .active{color:var(--blue)}
.login-btn{position:absolute;left:943px;top:18px;width:107px;height:31px;background:var(--green);border-bottom:2px solid var(--green-dark);color:#fff;font-size:11px;font-weight:600;text-align:center;line-height:30px}
.hero{position:absolute;top:69px;left:0;width:1200px;height:142px;background:linear-gradient(100deg,#141b28 0%,#263042 55%,#1d2536 100%)}
.hero-title{position:absolute;left:149px;top:44px;font-size:40px;font-weight:300;color:#fff}
.hero-title b{font-weight:700}
.hero-list{position:absolute;left:797px;top:32px;list-style:none;color:#fff;font-size:18px;font-weight:300;line-height:26.5px}
.hero-list li{display:flex;align-items:center;gap:11px}
.hero-list svg{width:15px;height:15px}
.price-badge{position:absolute;left:947px;top:22px;width:104px;height:104px}
.intro{position:absolute;left:151px;top:255px;width:523px}
.intro h1{font-size:28px;font-weight:600;color:var(--ink);line-height:32px}
.intro h2{font-size:14.5px;font-weight:600;color:var(--green);margin-top:6px;letter-spacing:.2px}
.intro p{font-size:12.5px;color:var(--text);line-height:19.5px;text-align:justify;margin-top:24px}
.intro p + p{margin-top:21px}
.signup{position:absolute;left:735px;top:261px;width:315px;height:322px;background:var(--blue)}
.signup h3{height:56px;background:var(--blue-dark);color:#fff;font-size:19.5px;font-weight:600;text-align:center;line-height:58px}
.field{position:absolute;left:25px;width:265px;height:45px;background:#fff;display:flex;align-items:center;font-size:12px;color:#444}
.field .ico{width:41px;height:45px;background:#dfe2e4;display:flex;align-items:center;justify-content:center;margin-right:11px}
.f1{top:81px}.f2{top:138px}.f3{top:196px}
.signup-btn{position:absolute;left:25px;top:254px;width:265px;height:46px;background:var(--green);border-bottom:3px solid var(--green-dark);color:#fff;font-size:14.5px;font-weight:600;text-align:center;line-height:44px}
.products{position:absolute;top:640px;left:0;width:1200px;height:184px;background:var(--band)}
.product{position:absolute;top:-18px;width:150px;text-align:center}
.product .halo{width:150px;height:150px;border-radius:50%;background:linear-gradient(#fff 0%,var(--band) 50%);display:flex;align-items:center;justify-content:center}
.product .disc{width:126px;height:126px;border-radius:50%;background:var(--blue);display:flex;align-items:center;justify-content:center}
.product span{display:block;margin-top:3px;font-size:18px;font-weight:600;color:var(--ink);white-space:nowrap}
.op{position:absolute;top:30px;color:#d3d8db;font-size:46px;font-weight:700}
.subscribe{position:absolute;top:824px;left:0;width:1200px;height:198px;background:var(--green);text-align:center;color:#fff}
.subscribe h2{margin-top:26px;font-size:28px;font-weight:600}
.subscribe p{font-size:15px;margin-top:0}
.sub-form{position:absolute;left:411px;top:115px;width:378px;height:45px;display:flex}
.sub-form .input{flex:1;background:#fff;color:#888;font-size:12px;text-align:left;padding-left:16px;line-height:45px}
.sub-form .btn{width:102px;background:#bcc3c6;font-size:12px;font-weight:600;line-height:45px}
.social{position:absolute;top:1047px;left:492px;display:flex;gap:26px}
.social i{display:block;width:14px;height:14px;border-radius:50%;background:#9a9ea2}
.rule{position:absolute;top:1084px;left:0;width:1200px;height:1px;background:#e6e6e6}
.foot-nav{position:absolute;top:1104px;width:1200px;text-align:center;font-size:11px;color:#666}
.foot-nav a{color:inherit;text-decoration:none;margin:0 6px}
.foot-nav a.active{color:var(--blue)}
.copy{position:absolute;top:1124px;width:1200px;text-align:center;font-size:11px;color:#666}
.copy span{color:var(--blue)}
</style>
</head>
<body>
<div class="page">
  <header class="site-header">
    <div class="brand"><span class="brand-dot"></span>VEXAWATCH.CO.UK</div>
    <nav class="main-nav"><span>HOME</span><span class="active">SOCIAL</span><span>ID ALERT</span><span>BANK ALERT</span><span>SIGNUP</span><span>CONTACT</span></nav>
    <div class="login-btn">MEMBER LOGIN</div>
  </header>

  <section class="hero">
    <div class="hero-title">Social <b>Alert!</b></div>
    <ul class="hero-list">
      <li><svg viewBox="0 0 16 16"><circle cx="8" cy="8" r="7" fill="none" stroke="#049dd9" stroke-width="1.5"/><path d="M6.5 4.8 9.7 8l-3.2 3.2" fill="none" stroke="#049dd9" stroke-width="1.5"/></svg>MONITORING</li>
      <li><svg viewBox="0 0 16 16"><circle cx="8" cy="8" r="7" fill="none" stroke="#049dd9" stroke-width="1.5"/><path d="M6.5 4.8 9.7 8l-3.2 3.2" fill="none" stroke="#049dd9" stroke-width="1.5"/></svg>INFORMING</li>
      <li><svg viewBox="0 0 16 16"><circle cx="8" cy="8" r="7" fill="none" stroke="#049dd9" stroke-width="1.5"/><path d="M6.5 4.8 9.7 8l-3.2 3.2" fill="none" stroke="#049dd9" stroke-width="1.5"/></svg>PROTECTING</li>
    </ul>
    <svg class="price-badge" viewBox="0 0 104 104">
      <polygon fill="#049dd9" points="52,0 58,9 67,2 70,13 80,9 80,20 91,20 88,30 98,33 92,42 101,48 93,55 100,63 90,67 94,77 83,79 84,90 73,89 70,99 61,94 55,104 49,95 41,102 37,92 27,96 26,85 15,86 17,75 6,72 12,63 2,57 10,50 3,42 13,38 9,28 20,26 19,15 30,17 32,6 42,10"/>
      <g transform="rotate(-25 52 52)" fill="#fff" font-family="Open Sans,Arial,sans-serif" text-anchor="middle">
        <text x="52" y="36" font-size="9">FOR ONLY</text>
        <text x="52" y="60" font-size="22" font-weight="600">£15.99</text>
        <text x="60" y="72" font-size="8">MONTH</text>
      </g>
    </svg>
  </section>

  <section class="intro">
    <h1>SOCIAL ALERT</h1>
    <h2>A PRODUCT TRULY DEVELOPED FOR THE 21ST CENTURY.</h2>
    <p>With the amount of information we freely make available today on sites such as Chatterlane, it's extremely important to be aware of not only what information we choose to share, but more importantly who we are sharing it with?. Online fraudsters are known to constantly search social media sites for profiles revealing personal information and this is often where thieves pick out their next unassuming and innocent victims.</p>
    <p>Using our specialist algorithms, we constantly monitor your social media activities and alert you when you share information that may be unwise and risky, after all prevention is better than cure.</p>
  </section>

  <aside class="signup">
    <h3>SIGNUP TO GET PROTECTED</h3>
    <div class="field f1"><span class="ico"><svg width="16" height="16" viewBox="0 0 16 16" fill="#fff"><circle cx="8" cy="5" r="3.5"/><path d="M1 16c0-4 3-6 7-6s7 2 7 6z"/></svg></span>FIRST NAME</div>
    <div class="field f2"><span class="ico"><svg width="16" height="16" viewBox="0 0 16 16" fill="#fff"><circle cx="8" cy="5" r="3.5"/><path d="M1 16c0-4 3-6 7-6s7 2 7 6z"/></svg></span>LASTE NAME</div>
    <div class="field f3"><span class="ico"><svg width="18" height="13" viewBox="0 0 18 13"><rect x=".5" y=".5" width="17" height="12" fill="#fff"/><path d="M.5.5 9 7 17.5.5" fill="none" stroke="#dfe2e4"/></svg></span>EMAIL ADDRESS</div>
    <div class="signup-btn">SIGN UP NOW!</div>
  </aside>

  <section class="products">
    <div class="product" style="left:223px"><div class="halo"><div class="disc">
      <svg width="82" height="74" viewBox="0 0 82 74">
        <g stroke="#fff" stroke-width="3" fill="none"><path d="M41 32 10 36"/><path d="M41 32 20 12"/><path d="M41 32 58 8"/><path d="M41 32 72 42"/><path d="M41 32 30 66"/></g>
        <g fill="#fff"><circle cx="10" cy="36" r="6"/><circle cx="20" cy="12" r="5"/><circle cx="58" cy="8" r="5"/><circle cx="72" cy="42" r="6"/><circle cx="30" cy="66" r="6"/>
        <circle cx="41" cy="22" r="6.5"/><path d="M28 42c0-10 26-10 26 0z"/></g>
      </svg>
    </div></div><span>Social Alert</span></div>
    <div class="op" style="left:378px">+</div>
    <div class="product" style="left:420px"><div class="halo"><div class="disc">
      <svg width="66" height="56" viewBox="0 0 66 56"><rect x="3" y="8" width="60" height="45" rx="6" fill="none" stroke="#fff" stroke-width="5"/><rect x="24" y="2" width="18" height="10" rx="2" fill="#fff"/><circle cx="22" cy="27" r="6" fill="#fff"/><path d="M11 44c0-8 22-8 22 0z" fill="#fff"/><rect x="38" y="25" width="16" height="5" rx="2" fill="#fff"/><rect x="38" y="35" width="16" height="5" rx="2" fill="#fff"/></svg>
    </div></div><span>ID Alert</span></div>
    <div class="op" style="left:576px">+</div>
    <div class="product" style="left:618px"><div class="halo"><div class="disc">
      <svg width="66" height="62" viewBox="0 0 66 62" fill="#fff"><path d="M33 2 64 18H2z"/><circle cx="33" cy="12" r="4" fill="#049dd9"/><rect x="6" y="22" width="54" height="4"/><rect x="9" y="29" width="6" height="22"/><rect x="51" y="29" width="6" height="22"/><rect x="19" y="29" width="5" height="22"/><rect x="42" y="29" width="5" height="22"/><text x="33" y="49" font-size="22" font-weight="700" text-anchor="middle" font-family="Open Sans,Arial,sans-serif">$</text><rect x="3" y="54" width="60" height="6"/></svg>
    </div></div><span>Bank Alert</span></div>
    <div class="op" style="left:778px;top:24px">=</div>
    <div class="product" style="left:827px"><div class="halo"><div class="disc"></div></div><span>Vexawatch.Co.Uk</span></div>
  </section>

  <section class="subscribe">
    <h2>SUBSCRIBE TO OUR UPDATES</h2>
    <p>Subscribe to your email newsletter for best venues</p>
    <div class="sub-form"><div class="input">ENTER YOUR EMAIL ID</div><div class="btn">SUBSCRIBE</div></div>
  </section>

  <div class="social"><i></i><i></i><i></i><i></i><i></i><i></i></div>
  <div class="rule"></div>
  <nav class="foot-nav"><a class="active">Home</a><a>Social</a><a>Id Alert</a><a>Bank Alert</a><a>Signup</a><a>Contact</a></nav>
  <p class="copy">Copyright © 2015 <span>Vexawatch</span>. All Rights Reserved</p>
</div>
</body>
</html>
```